Marketing / Informational Site for Marriage and Family Therapists Cooperative

We need a web design for a new Marriage and Family Therapist Cooperative, called Meadowlark Counselors. This is a market and information site for potential clients and referrals to learn more about the team and get contact information.

We are looking for profession, clean, and modern design, that cater towards families and mom's concerned about their families mental health and child development.

This should include a home page, an general about page, 3 bio pages (1 for each therapist listed below), and a general contact us page.

Our Domain Name

Meadowlarkcounselors.example

Company Name

Meadowlark Counselors

Group Moto/Philosophy

“Our sorrows and wounds are healed only when we touch them with compassion.” - Anonymous

Our Logo

See Heron Draft (attached)

Home Page (Introduction)

Feeling stressed and overwhelmed?
Encountering barriers towards your goals?
Having difficulty accomplishing the simplest task?
Have the need to talk but unsure who to turn to?

Therapy can assist you in overcoming all of these challenges. Assist you in uncovering the difficulties and barriers that are keeping you from achieving your life’s ambitions, help discover ways to overcome them, and cope with the impact your behaviour has on your occupation, personal life and social life.

Welcome to our practice, with over 20 years of combined experience in the clinical field you are sure to find the right fit for your needs. Each clinician has experience working with groups, adults, teens, children, families, and couples. We specialize in fostering healthy relationships between individuals, managing depression and anxiety, overcoming trauma, and developing occupational success. Feel free to explore information about each clinician and make an appointment with one of us today.

About Us (bio pics attached)

Marisol Dunkerly

My name is Dr. Marisol Dunkerly and I am a Licensed Marriage Family Therapist with a practice in Riverside, CA. I have devoted my life’s work into developing my skills in this profession. I have over 15 years of experience working in the clinical and the social service settings. These years have afforded me the opportunity to work with groups, families, adults, teens and children with varying symptoms. I have helped clients that have trauma, abuse histories, and many within the legal or social service systems. I enjoy working individuals from all walks of life achieve self sufficiency, social success and occupational success. In my years of training I have come to develop a culturally sensitive practice that centers around the needs of the client.

I have held many positions in my clinical career beginning as clinician moving upwards toward supervisor and program coordinator. I have also over 5 years of experience as an adjunct faculty member in the University setting teaching student to become Marriage and Family Therapists. As a clinician I focused on enriching my clinical skills by developing outcome driven practices to achieve client’s desired goals. As a clinical supervisor, I guided clinicians along their own paths towards clinical licensure. As a program coordinator, I helped develop a clinical assessment and triage program from ground up to assist client in accessing services in the South Los Angeles Area. The program would assist over 100 plus clients on a monthly basis get connected to clinical services and linked to any additional resources as needed by the individual. I have graduated with my, Bachelor’s degree at the Halvern State College, Westbrook. I received my Masters degree in Clinical Psychology at Mount St. Mary’s University, and my Doctorate degree in Clinical Psychology at Tolliver Institute.

To schedule an appointment with Dr. Marisol Dunkerly, LMFT:

email: marisol382@mailbox.example
Phone: (951)555-0182

Kit Osei

My name is Bernadette (Kit) Osei, I received my Masters Degree of Counseling in Marriage and Family Therapy from Calder Bay Polytechnic in June 2000. I have acquired over 15 years of experience helping Individuals, Couples, and Families cope with issues of Anxiety, Depression, Grief and Bereavement, and HIV/AIDS.

I am a Family Systems Therapist and I truly believe the dynamics in our family of origin greatly shape our current belief systems and behaviors. However, I often utilize a variety of approaches to help my clients achieve their goals depending on their individual needs.

My greatest strength as a Marriage and Family Therapist is helping my clients explore ways to make the changes in their lives that will allow them to live their life to their fullest potential. I help my clients achieve their personal life goals with a warm, safe, non-judgmental , and supportive environment. In doing so, my clients are encouraged to explore the issues that may be preventing them from living the life they desire. Thus, empowering them to take control of their personal journey to living a productive and meaningful life.

If you feel that you are ready to commit to bringing about positive changes in your life and would like support in exploring this path, I’m here to work with you in your journey to personal growth and development.

To schedule an appointment with Bernadette Osei, LMFT:

e-mail: bkit7@postbox.example
Phone: (951)555-0347

Greta Holmby

Greta Holmby graduated with a Masters in Marriage and Family Therapy from Fairhaven Ridge College. She currently holds a license in Marriage and Family Therapy in the State of California. She is also formally trained in Clinical Art Therapy. Greta's expertise lies in providing treatment to individuals experiencing work-related injuries, severe physical and emotional pain, trauma, grief and loss, anxiety and depression. In her early career, she provided valuable service at the largest free clinic in the nation serving marginalized families and children. For the past ten years, Greta has worked with HIV/AIDS population.
Greta comes from a multicultural background and she has utilized this experience and knowledge in serving a variety of populations. At an organizational level, Greta has worked extensively with challenging issues such as the chemical dependency and homelessness. In her private practice, Greta is proficient in working within individuals experiencing relationship concerns, marital and family conflict, depression/anxiety, self-esteem concerns, adjustment disorders, and pain management. She has treated clients from diverse cultural, linguistic backgrounds and sexual orientations.
Greta is trained in Family Systems Theory and incorporates other strategies appropriate for each presenting issue. She specializes in Clinical Art Therapy and has successfully utilized an integrated approach including guided imagery and relaxation skills training for many years.

To schedule an appointment with Greta Holmby, LMFT

e-mail: gretapaints@inkwell.example
Phone: (951) 555-0261

Target Market(s)

Families with child development, marriage issues, or other mental health needs

Industry/Entity Type

Marketing

Number of Pages Required

5+ page

Requirements
Must have
• 1 home page, 1 about page, 1 contact page. About page could either be standalone page with 3 different bio pages for each therapist or an all in one about page that includes bios for all 3 therapists.

```html
<!DOCTYPE html>
<html lang="en">
<head>
<meta charset="utf-8">
<title>Meadowlark Counselors</title>
<link rel="stylesheet" href="https://fonts.googleapis.com/css2?family=Roboto:wght@300;400;500;700&display=swap">
<style>
:root{
  --teal:#37b2c4;
  --pink:#d8428f;
  --magenta:#e45aa9;
  --blue:#6e8fdc;
  --ink:#4a4a4a;
  --muted:#8a8a8a;
  --light:#f5f3ea;
  --dark:#2d2a2e;
  --white:#ffffff;
}
*{box-sizing:border-box;margin:0;padding:0}
html,body{width:1200px;height:2868px;overflow:hidden}
body{font-family:"Roboto",Arial,sans-serif;color:var(--ink);background:var(--white);position:relative}
section,footer,header{position:relative;width:1200px;overflow:hidden}

/* hero */
.hero{height:536px}
.hero-photo{position:absolute;inset:0;background:
  linear-gradient(100deg,rgba(90,150,220,.85) 0%,rgba(140,130,210,.7) 45%,rgba(232,90,170,.85) 100%),
  radial-gradient(ellipse at 30% 70%,#c9a090 0%,#7a6a80 40%,#5a6fa8 80%)}
.nav{position:absolute;top:30px;left:240px;right:200px;display:flex;align-items:center;justify-content:space-between}
.brand{display:flex;align-items:center;gap:10px;color:var(--white);font-size:17px;font-weight:400;letter-spacing:.5px}
.brand-dot{width:14px;height:14px;border-radius:50%;background:var(--white)}
.menu{display:flex;align-items:center;gap:34px;font-size:12px;letter-spacing:1.5px;color:var(--white);font-weight:500}
.menu .pill{background:var(--teal);padding:8px 20px;border-radius:16px}
.quote{position:absolute;left:248px;top:176px;width:640px;color:var(--white);font-weight:300;font-size:30px;line-height:1.25}
.quote cite{display:block;font-style:normal;font-size:18px;margin-top:6px}
.btn{display:inline-block;font-size:12px;font-weight:500;letter-spacing:1.5px;color:var(--white);padding:11px 26px;border-radius:3px}
.hero .btn{position:absolute;left:248px;top:344px;background:var(--teal)}
.scroll-cue{position:absolute;left:584px;top:460px;width:32px;height:48px}

/* intro */
.intro{height:324px}
.intro-mark{position:absolute;left:0;right:0;top:44px;text-align:center;font-size:14px;letter-spacing:2px;color:var(--magenta);font-weight:500}
.intro-questions{position:absolute;left:240px;top:124px;width:440px;font-size:17px;font-weight:300;line-height:1.5;color:var(--ink);white-space:nowrap}
.intro-body{position:absolute;left:712px;top:124px;width:320px;font-size:12.5px;line-height:1.6;color:var(--muted)}

/* welcome */
.welcome{height:480px;background:var(--light)}
.section-title{text-align:center;font-weight:300;font-size:40px;color:#6b6b6b}
.welcome .section-title{position:absolute;top:26px;left:0;right:0}
.welcome-photo{position:absolute;left:360px;top:96px;width:480px;height:260px;border-radius:6px;
  background:radial-gradient(ellipse at 55% 45%,#efe6df 0%,#f7f3ef 50%,var(--light) 100%)}

/* services + team */
.practice{height:680px}
.practice-text{position:absolute;left:240px;top:48px;width:720px;text-align:center;font-size:12.5px;line-height:1.65;color:var(--muted)}
.timeline{position:absolute;left:240px;top:136px;width:720px;height:10px}
.pillars{position:absolute;left:240px;top:162px;width:720px;display:flex;justify-content:space-between}
.pillars p{width:190px;text-align:center;font-size:10.5px;font-weight:500;letter-spacing:1px;color:var(--pink);line-height:1.5}
.practice .section-title{position:absolute;top:270px;left:0;right:0}
.team{position:absolute;top:354px;left:0;right:0}
.member{position:absolute;width:220px;text-align:center;transform:translateX(-110px)}
.portrait{width:150px;height:150px;margin:0 auto;border-radius:50%;border:4px solid var(--magenta);padding:6px;background:var(--white)}
.portrait span{display:block;width:100%;height:100%;border-radius:50%;background:radial-gradient(circle at 50% 40%,#e8d6cc 0%,#b89484 45%,#d9d6d8 100%)}
.member h3{margin-top:22px;font-size:10.5px;font-weight:500;letter-spacing:1px;color:var(--pink)}
.stars{margin-top:10px;display:flex;justify-content:center;gap:8px}
.read-more{position:absolute;left:50%;top:120px;transform:translateX(-4px);background:var(--magenta);color:var(--white);font-size:10px;letter-spacing:1px;font-weight:500;padding:8px 16px;line-height:1.3;text-align:left;border-radius:2px}

/* family */
.family{height:392px}
.family-photo{position:absolute;inset:0;background:
  radial-gradient(ellipse at 66% 62%,#c9bfb6 0%,#dcd8d4 30%,transparent 55%),
  linear-gradient(180deg,#e4e4e6 0%,#f1f1f2 60%,#e7e7e9 100%)}
.family-text{position:absolute;left:200px;top:62px;width:300px;font-size:14px;line-height:1.6;color:var(--ink)}
.family .btn{position:absolute;left:200px;top:164px;background:var(--pink)}

/* footer */
.site-footer{height:376px}
.footer-map{position:absolute;inset:0;background:linear-gradient(115deg,var(--magenta) 0%,#d86cc0 40%,#8d8ee0 75%,var(--blue) 100%)}
.footer-info{position:absolute;left:0;right:0;top:56px;text-align:center;color:var(--white)}
.footer-info .brand{justify-content:center;font-size:18px}
.footer-info p{font-size:11.5px;letter-spacing:1px;line-height:1.9;margin-top:6px}
.footer-info .gap{margin-top:18px}
.bottom-bar{position:relative;height:80px;background:var(--dark)}
.socials{position:absolute;left:560px;top:-10px;display:flex;gap:16px}
.socials span{width:20px;height:20px;border-radius:50%;background:var(--magenta)}
.copyright{position:absolute;left:0;right:0;top:40px;text-align:center;font-size:9.5px;letter-spacing:1px;color:#9a959b}
</style>
</head>
<body>

<header class="hero">
  <div class="hero-photo" role="img" aria-label="Photo of a mother lifting her smiling child outdoors, tinted blue to pink"></div>
  <nav class="nav">
    <div class="brand"><span class="brand-dot"></span>Meadowlark Counselors</div>
    <div class="menu">
      <span>HOME</span><span>ABOUT US</span><span>BIOS</span><span class="pill">CONTACT US</span>
    </div>
  </nav>
  <blockquote class="quote">“Our sorrows and wounds are healed only when we touch them with compassion.”<cite>- Anonymous</cite></blockquote>
  <a class="btn">LEARN MORE</a>
  <svg class="scroll-cue" viewBox="0 0 32 48" aria-hidden="true">
    <circle cx="16" cy="16" r="14" fill="none" stroke="#fff" stroke-width="1.5"/>
    <path d="M10 13l6 6 6-6" fill="none" stroke="#fff" stroke-width="1.5"/>
    <rect x="6" y="40" width="20" height="2" fill="#fff" opacity=".7"/>
  </svg>
</header>

<section class="intro">
  <div class="intro-mark">MEADOWLARK COUNSELORS</div>
  <p class="intro-questions">Feeling stressed and overwhelmed?<br>Encountering barriers towards your goals?<br>Having difficulty accomplishing the simplest task?<br>Have the need to talk but unsure who to turn to?</p>
  <p class="intro-body">Therapy can assist you in overcoming all of these challenges. Assist you in uncovering the difficulties and barriers that are keeping you from achieving your life’s ambitions, help discover ways to overcome them, and cope with the impact your behaviour has on your occupation, personal life and social life.</p>
</section>

<section class="welcome">
  <h2 class="section-title">Welcome to our practice</h2>
  <div class="welcome-photo" role="img" aria-label="Photo of a smiling therapist working at a laptop"></div>
</section>

<section class="practice">
  <p class="practice-text">Welcome to our practice, with over 20 years of combined experience in the clinical field you are sure to find the right fit for your needs. Each clinician has experience working with groups, adults, teens, children, families, and couples. We specialize in fostering healthy relationships between individuals, managing depression and anxiety, overcoming trauma, and developing occupational success.</p>
  <svg class="timeline" viewBox="0 0 720 10" aria-hidden="true">
    <line x1="95" y1="5" x2="625" y2="5" stroke="#d8428f" stroke-width="1.5"/>
    <circle cx="95" cy="5" r="4.5" fill="#d8428f"/>
    <circle cx="360" cy="5" r="4.5" fill="#d8428f"/>
    <circle cx="625" cy="5" r="4.5" fill="#d8428f"/>
  </svg>
  <div class="pillars">
    <p>WE FOSTER HEALTHY<br>RELATIONSHIPS</p>
    <p>WE HELP MANAGE DEPRESSION,<br>ANXIETY &amp; OVERCOME TRAUMA</p>
    <p>WE DEVELOP YOUR<br>OCCUPATIONAL SUCCESS</p>
  </div>

  <h2 class="section-title">Meet the Team</h2>
  <div class="team">
    <div class="member" style="left:360px">
      <div class="portrait"><span role="img" aria-label="Portrait of Dr. Marisol Dunkerly"></span></div>
      <h3>DR. MARISOL DUNKERLY</h3>
      <div class="stars">
        <svg width="14" height="14" viewBox="0 0 24 24"><path d="M12 2l3 7h7l-5.5 4.5 2 7.5-6.5-4.5-6.5 4.5 2-7.5L2 9h7z" fill="#cfcfcf"/></svg>
        <svg width="14" height="14" viewBox="0 0 24 24"><path d="M12 2l3 7h7l-5.5 4.5 2 7.5-6.5-4.5-6.5 4.5 2-7.5L2 9h7z" fill="#cfcfcf"/></svg>
        <svg width="14" height="14" viewBox="0 0 24 24"><path d="M12 2l3 7h7l-5.5 4.5 2 7.5-6.5-4.5-6.5 4.5 2-7.5L2 9h7z" fill="#cfcfcf"/></svg>
        <svg width="14" height="14" viewBox="0 0 24 24"><path d="M12 2l3 7h7l-5.5 4.5 2 7.5-6.5-4.5-6.5 4.5 2-7.5L2 9h7z" fill="#cfcfcf"/></svg>
      </div>
    </div>
    <div class="member" style="left:600px">
      <div class="portrait"><span role="img" aria-label="Portrait of Bernadette (Kit) Osei"></span></div>
      <div class="read-more">READ<br>MORE</div>
      <h3>BERNADETTE (KIT) OSEI</h3>
      <div class="stars">
        <svg width="14" height="14" viewBox="0 0 24 24"><path d="M12 2l3 7h7l-5.5 4.5 2 7.5-6.5-4.5-6.5 4.5 2-7.5L2 9h7z" fill="#cfcfcf"/></svg>
        <svg width="14" height="14" viewBox="0 0 24 24"><path d="M12 2l3 7h7l-5.5 4.5 2 7.5-6.5-4.5-6.5 4.5 2-7.5L2 9h7z" fill="#cfcfcf"/></svg>
        <svg width="14" height="14" viewBox="0 0 24 24"><path d="M12 2l3 7h7l-5.5 4.5 2 7.5-6.5-4.5-6.5 4.5 2-7.5L2 9h7z" fill="#cfcfcf"/></svg>
        <svg width="14" height="14" viewBox="0 0 24 24"><path d="M12 2l3 7h7l-5.5 4.5 2 7.5-6.5-4.5-6.5 4.5 2-7.5L2 9h7z" fill="#cfcfcf"/></svg>
      </div>
    </div>
    <div class="member" style="left:840px">
      <div class="portrait"><span role="img" aria-label="Portrait of Greta Holmby"></span></div>
      <h3>GRETA HOLMBY</h3>
      <div class="stars">
        <svg width="14" height="14" viewBox="0 0 24 24"><path d="M12 2l3 7h7l-5.5 4.5 2 7.5-6.5-4.5-6.5 4.5 2-7.5L2 9h7z" fill="#cfcfcf"/></svg>
        <svg width="14" height="14" viewBox="0 0 24 24"><path d="M12 2l3 7h7l-5.5 4.5 2 7.5-6.5-4.5-6.5 4.5 2-7.5L2 9h7z" fill="#cfcfcf"/></svg>
        <svg width="14" height="14" viewBox="0 0 24 24"><path d="M12 2l3 7h7l-5.5 4.5 2 7.5-6.5-4.5-6.5 4.5 2-7.5L2 9h7z" fill="#cfcfcf"/></svg>
        <svg width="14" height="14" viewBox="0 0 24 24"><path d="M12 2l3 7h7l-5.5 4.5 2 7.5-6.5-4.5-6.5 4.5 2-7.5L2 9h7z" fill="#cfcfcf"/></svg>
      </div>
    </div>
  </div>
</section>

<section class="family">
  <div class="family-photo" role="img" aria-label="Photo of a family of three seated on white chairs holding hands"></div>
  <p class="family-text">Feel free to explore information about each clinician and make an appointment with one of us today.</p>
  <a class="btn">CONTACT US TODAY</a>
</section>

<footer class="site-footer">
  <div class="footer-map" role="img" aria-label="Faint street map of the practice area on a pink to blue gradient"></div>
  <div class="footer-info">
    <div class="brand"><span class="brand-dot"></span>Meadowlark Counselors</div>
    <p class="gap">MEADOWLARK COUNSELORS<br>4820 ALDER GROVE AVE, SUITE 210, RIVERSIDE, CA 92501<br>PHONE: (951) 555-0100</p>
    <p class="gap">HELLO@MEADOWLARKCOUNSELORS.EXAMPLE<br>MEADOWLARKCOUNSELORS.EXAMPLE</p>
  </div>
</footer>
<div class="bottom-bar">
  <div class="socials"><span></span><span></span><span></span></div>
  <p class="copyright">© 2016 MEADOWLARK COUNSELORS. ALL RIGHTS RESERVED.</p>
</div>

</body>
</html>
```